Brindle Logistics Business Card Design

We are a trucking and warehousing company. We run freight in the US manly from the Pacific NW to TX and back up the the PNW. We also do warehousing where we store, move, and distribute freight. Looking for a clean and modern design of business card. We would like to look rich and elegant. Attached is our logo.

Industry/Entity Type

Trucking Company

Contact Information for Business Card

Looking for a clean and modern design of business card. We would like to look rich and elegant.

Font styles to use
Sans Serif

Colors

Designer to choose colors to be used in the design.

Requirements
Must have
• logo but it should not dominate the card
Should not have
• logo should not dominate the card

```html
<!DOCTYPE html>
<html lang="en">
<head>
<meta charset="utf-8">
<title>Brindle Logistics Business Cards</title>
<link href="https://fonts.googleapis.com/css2?family=Open+Sans:wght@400;600;700&display=swap" rel="stylesheet">
<style>
  :root {
    --bg: #dcdddf;
    --card: #ffffff;
    --card-dark: #1c1b1d;
    --ink: #3c3c3c;
    --blue: #0f6fb8;
    --orange: #f39a1f;
    --faint: #0e0e0f;
  }
  * { margin: 0; padding: 0; box-sizing: border-box; }
  html, body { width: 1042px; height: 1200px; overflow: hidden; background: var(--bg); }
  body { position: relative; font-family: "Open Sans", sans-serif; color: var(--ink); }
  .card { position: absolute; background: var(--card); box-shadow: 0 1px 4px rgba(0,0,0,.12); overflow: hidden; }
  .card--dark { background: var(--card-dark); }
  .h { width: 370px; height: 210px; }
  .v { width: 210px; height: 370px; }
  .abs { position: absolute; }
  .center { left: 0; right: 0; text-align: center; }

  .brand { display: flex; align-items: center; gap: 8px; font-weight: 700; color: var(--ink); white-space: nowrap; }
  .brand__mark { width: 14px; height: 14px; background: var(--blue); flex: none; }
  .brand--dark { color: var(--faint); }
  .brand--dark .brand__mark { display: none; }

  .name { font-weight: 700; font-size: 12.5px; color: var(--blue); letter-spacing: .2px; line-height: 1; }
  .name--plain { color: var(--ink); font-weight: 600; text-transform: none; }
  .title { font-size: 9.5px; line-height: 1; }
  .info { font-size: 9.5px; line-height: 13.6px; }
  .url { font-size: 9.5px; letter-spacing: 1.2px; }
  .rule { position: absolute; background: var(--ink); height: 1px; }
  .row { display: flex; align-items: center; gap: 4px; }
  .icon { width: 9px; height: 9px; flex: none; }
  .hexes { display: flex; justify-content: center; gap: 3px; }
  .hex { width: 17px; height: 18px; }
</style>
</head>
<body>
<svg width="0" height="0" style="position:absolute">
  <defs>
    <symbol id="i-phone" viewBox="0 0 16 16"><path d="M4 1.5l2.2 3-1.3 1.6c.8 1.8 2.2 3.3 4.1 4.2l1.6-1.3 3 2.2-1.3 2.6C6.5 13.6 2.4 9.5 1.5 3z" fill="currentColor"/></symbol>
    <symbol id="i-mail" viewBox="0 0 16 16"><rect x="1.5" y="3.5" width="13" height="9" fill="currentColor"/><path d="M1.8 4l6.2 4.6L14.2 4" stroke="#fff" stroke-width="1.2" fill="none"/></symbol>
    <symbol id="i-globe" viewBox="0 0 16 16"><g fill="none" stroke="currentColor" stroke-width="1.3"><circle cx="8" cy="8" r="6"/><ellipse cx="8" cy="8" rx="2.6" ry="6"/><path d="M2 8h12M3 5h10M3 11h10"/></g></symbol>
    <symbol id="i-pin" viewBox="0 0 16 16"><path d="M8 1.5a4.5 4.5 0 0 0-4.5 4.5C3.5 9.5 8 14.5 8 14.5s4.5-5 4.5-8.5A4.5 4.5 0 0 0 8 1.5zm0 6.3a1.8 1.8 0 1 1 0-3.6 1.8 1.8 0 0 1 0 3.6z" fill="currentColor"/></symbol>
    <symbol id="hex-blue" viewBox="0 0 20 22"><path d="M10 1l8.5 5v10L10 21l-8.5-5V6z" fill="#fff" stroke="#0f6fb8" stroke-width="1.3"/></symbol>
  </defs>
</svg>

<!-- Front, landscape -->
<section class="card h" style="left:143px;top:173px">
  <div class="abs brand" style="left:86px;top:90px;font-size:22px"><span class="brand__mark"></span>Brindle Logistics</div>
  <p class="abs center url" style="top:183px">www.BRINDLELOGISTICS.com</p>
</section>

<!-- Back, dark landscape -->
<section class="card card--dark h" style="left:143px;top:399px">
  <div class="abs brand brand--dark" style="left:62px;top:86px;font-size:29px">Brindle Logistics</div>
</section>

<!-- Layout A -->
<section class="card h" style="left:545px;top:59px">
  <p class="abs center name" style="top:76px">YOUR NAME</p>
  <p class="abs center title" style="top:91px">Title</p>
  <div class="rule" style="left:42px;width:286px;top:136px"></div>
  <div class="abs info" style="left:42px;top:143px">
    <div class="row"><svg class="icon" style="color:var(--orange)"><use href="#i-phone"/></svg>123.456.7890</div>
    <div class="row"><svg class="icon" style="color:var(--orange)"><use href="#i-mail"/></svg>name@BrindleLogistics.com</div>
  </div>
  <div class="abs info" style="right:42px;top:143px;text-align:right">123 Main Street<br>Dallas, TX 75207</div>
</section>

<!-- Layout B -->
<section class="card h" style="left:545px;top:286px">
  <div class="abs" style="right:196px;top:88px;text-align:right">
    <p class="name">YOUR NAME</p>
    <p class="title" style="margin-top:5px">Title</p>
  </div>
  <div class="abs" style="left:184px;top:86px;width:1px;height:40px;background:var(--ink)"></div>
  <div class="abs info" style="left:195px;top:92px">123.456.7890<br>name@BrindleLogistics.com</div>
</section>

<!-- Layout C -->
<section class="card h" style="left:545px;top:512px">
  <div class="abs brand" style="left:14px;top:35px;font-size:20px"><span class="brand__mark"></span>Brindle Logistics</div>
  <div class="abs" style="left:346px;top:0;width:4px;height:210px;background:var(--blue)"></div>
  <div class="abs" style="right:34px;top:101px;text-align:right">
    <p class="name">YOUR NAME</p>
    <p class="title" style="margin-top:4px">Title</p>
  </div>
  <div class="abs info" style="right:34px;top:136px;text-align:right;line-height:15.2px">
    123.456.7890<br>name@BrindleLogistics.com<br>www.BrindleLogistics.com<br>123 Main Street, Dallas, TX 75207
  </div>
  <div class="abs" style="left:339px;top:136px;display:flex;flex-direction:column;gap:0">
    <svg class="hex" viewBox="0 0 20 22" style="width:15px;height:15.2px;color:var(--orange)"><use href="#hex-blue"/><use href="#i-phone" x="5" y="6" width="10" height="10"/></svg>
    <svg class="hex" viewBox="0 0 20 22" style="width:15px;height:15.2px;color:var(--orange)"><use href="#hex-blue"/><use href="#i-mail" x="5" y="6" width="10" height="10"/></svg>
    <svg class="hex" viewBox="0 0 20 22" style="width:15px;height:15.2px;color:var(--orange)"><use href="#hex-blue"/><use href="#i-globe" x="5" y="6" width="10" height="10"/></svg>
    <svg class="hex" viewBox="0 0 20 22" style="width:15px;height:15.2px;color:var(--orange)"><use href="#hex-blue"/><use href="#i-pin" x="5" y="6" width="10" height="10"/></svg>
  </div>
</section>

<!-- Portrait back, dark -->
<section class="card card--dark v" style="left:60px;top:770px">
  <div class="abs brand brand--dark" style="left:0;right:0;top:176px;justify-content:center;font-size:22px">Brindle Logistics</div>
</section>

<!-- Portrait front with details -->
<section class="card v" style="left:286px;top:770px">
  <div class="abs brand" style="left:0;right:0;top:82px;justify-content:center;font-size:17px"><span class="brand__mark"></span>Brindle Logistics</div>
  <p class="abs center name name--plain" style="top:177px">Your Name</p>
  <p class="abs center title" style="top:193px">Title</p>
  <div class="rule" style="left:36px;width:139px;top:216px"></div>
  <p class="abs center info" style="top:228px">123 Main Street<br>Dallas, TX 75207</p>
  <div class="abs center hexes" style="top:267px">
    <svg class="hex" viewBox="0 0 20 22" style="color:var(--blue)"><use href="#hex-blue"/><use href="#i-phone" x="5" y="6" width="10" height="10"/></svg>
    <svg class="hex" viewBox="0 0 20 22" style="color:var(--blue)"><use href="#hex-blue"/><use href="#i-mail" x="5" y="6" width="10" height="10"/></svg>
    <svg class="hex" viewBox="0 0 20 22" style="color:var(--blue)"><use href="#hex-blue"/><use href="#i-globe" x="5" y="6" width="10" height="10"/></svg>
  </div>
  <p class="abs center info" style="top:296px">123.456.7890<br>name@BrindleLogistics.com<br>www.BrindleLogistics.com</p>
  <div class="abs" style="left:0;right:0;bottom:0;height:6px;background:var(--blue)"></div>
</section>

<!-- Portrait front, logo only -->
<section class="card v" style="left:545px;top:770px">
  <div class="abs brand" style="left:0;right:0;top:176px;justify-content:center;font-size:17px"><span class="brand__mark"></span>Brindle Logistics</div>
</section>

<!-- Portrait back, details -->
<section class="card v" style="left:771px;top:770px">
  <p class="abs center name name--plain" style="top:110px">Your Name</p>
  <p class="abs center title" style="top:126px">Title</p>
  <div class="abs" style="left:89px;width:32px;top:149px;height:1.5px;background:var(--orange)"></div>
  <p class="abs center info" style="top:159px">123 Main Street<br>Dallas, TX 75207</p>
  <div class="abs center hexes" style="top:198px">
    <svg class="hex" viewBox="0 0 20 22" style="color:var(--blue)"><use href="#hex-blue"/><use href="#i-phone" x="5" y="6" width="10" height="10"/></svg>
    <svg class="hex" viewBox="0 0 20 22" style="color:var(--blue)"><use href="#hex-blue"/><use href="#i-mail" x="5" y="6" width="10" height="10"/></svg>
    <svg class="hex" viewBox="0 0 20 22" style="color:var(--blue)"><use href="#hex-blue"/><use href="#i-globe" x="5" y="6" width="10" height="10"/></svg>
  </div>
  <p class="abs center info" style="top:228px">123.456.7890<br>name@BrindleLogistics.com<br>www.BrindleLogistics.com</p>
</section>
</body>
</html>
```